Business Card Design

Want something very unique. No business, just personal. The image I submitted is for inspiration only.

Target Market(s)

friends and new acquaintances

Industry/Entity Type

Business

Contact Information for Business Card

Mara Deltow
Alder Mesa, NM
505-271-4906
maradeltow@quillbox.net

```html
<!DOCTYPE html>
<html lang="en">
<head>
<meta charset="utf-8">
<title>Mara Deltow — Personal Card</title>
<link href="https://fonts.googleapis.com/css2?family=Fira+Sans+Condensed:wght@700&family=Fira+Sans:wght@400&display=swap" rel="stylesheet">
<style>
  :root {
    --backdrop: #7d1f22;
    --card-white: #ffffff;
    --card-grey: #ededed;
    --soft-ring: #f4f4f4;
    --ink: #111111;
    --dot-tone: #6e6e6e;
    --photo-earth: #8a4b2c;
    --photo-sand: #c9a273;
    --photo-leaf: #8d9a63;
  }
  html, body {
    margin: 0;
    width: 1200px;
    height: 898px;
    overflow: hidden;
    background: var(--backdrop);
  }
  .card {
    position: absolute;
    left: 377px;
    top: 59px;
    width: 446px;
    height: 780px;
    background: var(--card-white);
    overflow: hidden;
    box-shadow: 0 10px 30px rgba(0,0,0,.35);
  }
  .card__chevron-zone {
    position: absolute;
    left: 0; top: 0;
    width: 100%; height: 150px;
    background: var(--card-grey);
  }
  .card__chevron-zone svg { display: block; }
  .card__photo {
    position: absolute;
    left: 0; top: 150px;
    width: 100%; height: 290px;
    background:
      radial-gradient(ellipse at 45% 60%, var(--photo-sand) 0%, transparent 55%),
      linear-gradient(160deg, var(--photo-leaf) 0%, var(--photo-earth) 55%, #6b3a24 100%);
  }
  .card__details {
    position: absolute;
    left: 0; top: 440px;
    width: 100%; height: 220px;
    background: var(--card-white);
    overflow: hidden;
  }
  .card__ring {
    position: absolute;
    left: 123px; top: -40px;
    width: 200px; height: 200px;
    border-radius: 50%;
    background: var(--soft-ring);
  }
  .card__text {
    position: relative;
    padding: 34px 28px 0 30px;
    color: var(--ink);
  }
  .card__name {
    font-family: "Fira Sans Condensed", sans-serif;
    font-weight: 700;
    font-size: 27px;
    margin: 0 0 22px;
    white-space: nowrap;
  }
  .card__line {
    font-family: "Fira Sans", sans-serif;
    font-weight: 400;
    font-size: 27px;
    margin: 0 0 16px;
    white-space: nowrap;
  }
  .card__dot-band {
    position: absolute;
    left: 0; bottom: 0;
    width: 100%; height: 120px;
    background: linear-gradient(180deg, #b5b5b5 0%, var(--dot-tone) 100%);
  }
</style>
</head>
<body>
  <div class="card">
    <div class="card__chevron-zone">
      <svg width="446" height="150" viewBox="0 0 446 150" role="img" aria-label="Halftone dot chevron band">
        <polygon points="0,0 60,0 223,110 386,0 446,0 446,40 223,150 0,40" fill="#8a8a8a"/>
      </svg>
    </div>
    <div class="card__photo" role="img" aria-label="Photo of two people crouching beside cheetahs in a fenced enclosure"></div>
    <div class="card__details">
      <div class="card__ring"></div>
      <div class="card__text">
        <p class="card__name">Mara Deltow Alder Mesa, NM</p>
        <p class="card__line">505-271-4906</p>
        <p class="card__line">maradeltow@quillbox.net</p>
      </div>
    </div>
    <div class="card__dot-band" role="img" aria-label="Halftone dot pattern band"></div>
  </div>
</body>
</html>
```